International Firefighter Competition Needs New Website that Looks Like It's a Global Sportin...

The Blazeguard Relay is held globally and sees thousands of firefighters competing on an obstacle course known as the toughest two minutes in sports. This year the organization received a makeover with new logo and new look of our challenge course. We also introduced the Blazeguard Relay Circuit (known as the BRC). We envision a new website that inspires our next generation of competitors! It's time to wow them visually and to make them feel that this exciting sport proudly represents them as our global heroes that protect each and every one of us in a moments notice! NOTE: Photos provided are just for you to use as placeholders. TO SEE A VIDEO OF OUR EVENT: https://clipvault-example.net/734205918

NOTE: In 2023 we sub-divided the U.S. into 5 new regions for the BRC: Blazeguard Relay Circuit. I've now added these logos in the event a designer sees a vision of integrating these.

Target Market(s)

Firefighters and Sponsors

Coding

Coded - Design and coding required

Requirements
Must have
• Rival other major sporting event websites. See attached samples.
Nice to have
• No suggestions. We truly are open to creativity.
Should not have
• Too firefighter looking. Needs to be the perfect blend of promoting our firefighters as athletes in our sport.

```html
<!DOCTYPE html>
<html lang="en">
<head>
<meta charset="utf-8">
<title>Blazeguard Relay</title>
<link href="https://fonts.googleapis.com/css2?family=Oswald:wght@300;400;500;600;700&family=Poppins:wght@400&display=swap" rel="stylesheet">
<style>
  :root {
    --red: #d42e36;
    --red-deep: #c2262f;
    --blue: #1a8fd6;
    --navy: #12355b;
    --white: #ffffff;
    --ink: #3c3c3c;
    --photo-dark: #1b1f26;
    --photo-mid: #3a4452;
  }
  * { margin: 0; padding: 0; box-sizing: border-box; }
  html, body { width: 1200px; height: 692px; overflow: hidden; background: var(--white); }
  body { position: relative; font-family: 'Oswald', sans-serif; }

  .site-header { position: absolute; top: 0; left: 0; width: 1200px; height: 88px; background: var(--white); z-index: 3; }
  .brand {
    position: absolute; left: 148px; top: 22px; display: flex; align-items: center; gap: 8px;
    font-family: 'Oswald', sans-serif; font-weight: 600; font-size: 22px; line-height: 1;
    color: var(--navy); text-transform: uppercase;
  }
  .brand-mark { width: 26px; height: 26px; background: var(--red); }
  .main-nav { position: absolute; top: 0; left: 0; }
  .nav-link {
    position: absolute; top: 37px; font-weight: 500; font-size: 17.5px; line-height: 1;
    color: var(--blue); text-decoration: none; text-transform: uppercase; white-space: nowrap;
  }
  .nav-link.is-active { color: var(--red); }
  .nav-link.is-active::before {
    content: ""; position: absolute; left: 0; top: -7px; width: 34px; height: 3px; background: var(--blue);
  }
  .circuit-badge {
    position: absolute; left: 970px; top: 33px; display: flex; align-items: center; gap: 7px;
    font-weight: 600; font-size: 20px; line-height: 1; color: var(--red);
  }
  .circuit-badge .badge-mark { width: 22px; height: 22px; background: var(--blue); }

  .hero { position: absolute; top: 88px; left: 0; width: 1200px; height: 550px; overflow: hidden; }
  .hero-photo {
    position: absolute; inset: 0;
    background:
      radial-gradient(ellipse 260px 300px at 340px 260px, #4a5260 0%, rgba(74,82,96,0) 70%),
      radial-gradient(ellipse 500px 180px at 420px 500px, rgba(170,180,190,.55) 0%, rgba(170,180,190,0) 70%),
      linear-gradient(100deg, var(--photo-mid) 0%, var(--photo-dark) 55%, #0f1318 100%);
  }
  .hero-shape { position: absolute; inset: 0; }
  .social-links { position: absolute; left: 26px; top: 222px; display: flex; flex-direction: column; gap: 19px; }
  .social-links span { display: block; width: 13px; height: 13px; border-radius: 50%; background: var(--white); }

  .hero-content { position: absolute; left: 746px; top: 132px; width: 420px; }
  .hero-title {
    font-weight: 700; font-style: italic; font-size: 70px; line-height: 70px;
    text-transform: uppercase; letter-spacing: -0.5px;
    background: linear-gradient(118deg, var(--blue) 0 44%, var(--white) 44% 100%);
    -webkit-background-clip: text; background-clip: text; color: transparent;
    transform: skewX(-6deg);
  }
  .hero-title span { display: block; }
  .hero-text {
    margin-top: 17px; font-family: 'Poppins', sans-serif; font-size: 15.5px; line-height: 18px; color: var(--white);
  }
  .hero-cta {
    position: absolute; left: 0; top: 305px; width: 162px; height: 58px; border: 3px solid var(--white);
    border-radius: 29px; background: linear-gradient(90deg, #b8343a 0%, #7f4a73 50%, #2f7fc4 100%);
    display: flex; align-items: center; padding-left: 15px;
    color: var(--white); font-weight: 500; font-size: 19px; text-decoration: none; text-transform: uppercase;
  }
  .hero-cta .cta-arrow {
    position: absolute; right: 8px; top: 8px; width: 36px; height: 36px; border-radius: 50%; background: var(--red);
    display: flex; align-items: center; justify-content: center;
  }

  .site-footer { position: absolute; left: 0; top: 638px; width: 1200px; height: 54px; background: var(--white); }
  .footer-call {
    position: absolute; left: 0; top: 0; width: 334px; height: 54px; background: var(--red);
    clip-path: polygon(0 0, 100% 0, 90% 100%, 0 100%);
    display: flex; align-items: center; padding-left: 30px; gap: 9px;
    color: var(--white); font-weight: 500; font-size: 24px; line-height: 1;
  }
  .footer-video {
    position: absolute; left: 347px; top: 17px; display: flex; align-items: center; gap: 9px;
    font-weight: 300; font-size: 14px; line-height: 20px; color: var(--ink); text-decoration: none;
  }
  .footer-video .video-mark { width: 20px; height: 18px; background: var(--red); border-radius: 3px; }
  .footer-copy {
    position: absolute; right: 148px; top: 17px; font-weight: 300; font-size: 14px; line-height: 20px;
    color: var(--ink); text-transform: uppercase;
  }
</style>
</head>
<body>
  <header class="site-header">
    <div class="brand"><span class="brand-mark"></span>Blazeguard Relay</div>
    <nav class="main-nav">
      <a class="nav-link is-active" href="#" style="left:386px">Home</a>
      <a class="nav-link" href="#" style="left:460px">About Us</a>
      <a class="nav-link" href="#" style="left:566px">Our Events</a>
      <a class="nav-link" href="#" style="left:681px">Training</a>
      <a class="nav-link" href="#" style="left:779px">News</a>
      <a class="nav-link" href="#" style="left:853px">Contact</a>
    </nav>
    <div class="circuit-badge"><span class="badge-mark"></span>BRC</div>
  </header>

  <section class="hero">
    <div class="hero-photo" role="img" aria-label="Firefighter athlete in full turnout gear and breathing mask standing in smoke inside a fire station"></div>
    <svg class="hero-shape" width="1200" height="550" viewBox="0 0 1200 550" aria-hidden="true">
      <defs>
        <linearGradient id="heroRed" x1="0" y1="0" x2="1" y2="1">
          <stop offset="0" stop-color="#d8323a"/>
          <stop offset="1" stop-color="#c4262e"/>
        </linearGradient>
      </defs>
      <path d="M825 0 C 810 55 745 105 718 150 C 696 190 718 240 690 290 C 655 345 592 380 598 440 C 604 495 735 505 750 550 L1200 550 L1200 0 Z" fill="url(#heroRed)"/>
    </svg>

    <div class="social-links" aria-label="Social links">
      <span></span><span></span><span></span>
    </div>

    <div class="hero-content">
      <h1 class="hero-title"><span>Blazeguard</span><span>Relay</span></h1>
      <p class="hero-text">Lorem ipsum dolor sit amet, consectetur<br>adipiscing elit, sed do eiusmod.</p>
      <a class="hero-cta" href="#">Our Events
        <span class="cta-arrow">
          <svg width="20" height="18" viewBox="0 0 20 18" aria-hidden="true"><path d="M2 9H17M10 2L17 9L10 16" stroke="#fff" stroke-width="3" fill="none" stroke-linecap="round" stroke-linejoin="round"/></svg>
        </span>
      </a>
    </div>
  </section>

  <footer class="site-footer">
    <div class="footer-call">
      <svg width="17" height="17" viewBox="0 0 24 24" aria-hidden="true"><path fill="#fff" d="M6.6 10.8c1.4 2.8 3.8 5.1 6.6 6.6l2.2-2.2c.3-.3.7-.4 1-.2 1.1.4 2.3.6 3.6.6.6 0 1 .4 1 1V20c0 .6-.4 1-1 1C10.6 21 3 13.4 3 4c0-.6.4-1 1-1h3.5c.6 0 1 .4 1 1 0 1.2.2 2.4.6 3.6.1.3 0 .7-.2 1L6.6 10.8z"/></svg>
      CALL US: 123 456 7890
    </div>
    <a class="footer-video" href="https://clipvault-example.net/734205918"><span class="video-mark"></span>OUR EVENTS</a>
    <p class="footer-copy">Copyright © 2023 All rights reserved.</p>
  </footer>
</body>
</html>
```